Online Art Gallery & Art Management Firm looking for a business card

I'm launching an online art gallery (paintings, photography, drawings, furniture, books, ...) where people can buy all types of art. It's a platform where young and unknown artists can showcase their oeuvre.

Additionally, the venture will act as my advising company for artists. I help them out with their business side of life and become their representative.

The company name: The Velvet Parlour
Logo is attached

I'm looking for something very classy and upmarket.
Updates

Reason: Logo wasn't finished yet...

The design should include the following information: - Name: Pieter Vandomme - Title: Founder - Mobile: +32 (0) 486 514 362 - E-mail: pieter@velvet-parlour.example - Website www.velvet-parlour.example I prefer the have the logo (without website) on the one side and the information on the other. Best regards Pieter

Target Market(s)

Art buyers / art dealers / artists / middle class / upmarket /

Industry/Entity Type

Artists

Colors

Designer to choose colors to be used in the design.

Requirements
Must have
• Must communicate credibility, trust and integrity
Nice to have
• Something classy, chique
Should not have
• Nothing to artistic or creative

```html
<!DOCTYPE html>
<html lang="en">
<head>
<meta charset="utf-8">
<title>The Velvet Parlour – Business Card</title>
<link rel="stylesheet" href="https://fonts.googleapis.com/css2?family=Josefin+Sans:wght@300&family=Cormorant+Garamond:wght@500&family=Montserrat:wght@700&display=swap">
<style>
  :root {
    --backdrop: #c9c9c9;
    --ink-black: #050505;
    --soft-black: #161616;
    --paper-white: #f1f1f1;
    --logo-dark: #1a1a1a;
    --logo-light: #f4f4f4;
    --detail-grey: #b9b9b9;
    --name-grey: #a9a9a9;
  }
  * { margin: 0; padding: 0; box-sizing: border-box; }
  html, body {
    width: 1200px; height: 1000px; overflow: hidden;
    background: var(--backdrop);
  }
  .card {
    position: absolute;
    left: 210px;
    width: 780px; height: 446px;
    border-radius: 28px;
    overflow: hidden;
    box-shadow: 0 6px 18px rgba(0,0,0,0.25);
  }
  .card--front { top: 28px; }
  .card--back { top: 522px; }
  .card__art { position: absolute; inset: 0; width: 100%; height: 100%; }

  .wordmark {
    position: absolute;
    font-family: "Josefin Sans", sans-serif;
    font-weight: 300;
    text-transform: uppercase;
    letter-spacing: 0.2em;
    white-space: nowrap;
  }
  .card--front .wordmark {
    left: 0; width: 540px; top: 196px;
    text-align: center;
    font-size: 34px;
    color: var(--logo-dark);
  }
  .card--back .wordmark {
    left: 46px; top: 52px;
    font-size: 27px;
    color: var(--logo-light);
  }

  .holder { position: absolute; left: 46px; top: 150px; }
  .holder__name {
    font-family: "Cormorant Garamond", serif;
    font-weight: 500;
    font-size: 28px;
    letter-spacing: 0.04em;
    color: var(--name-grey);
  }
  .holder__title {
    font-family: "Montserrat", sans-serif;
    font-weight: 700;
    font-size: 11px;
    letter-spacing: 0.2em;
    color: var(--name-grey);
    margin-top: 2px;
  }

  .contacts {
    position: absolute; left: 46px; top: 232px;
    list-style: none;
  }
  .contacts__item {
    display: flex; align-items: center;
    height: 34px;
    font-family: "Cormorant Garamond", serif;
    font-weight: 500;
    font-size: 19px;
    letter-spacing: 0.03em;
    color: var(--detail-grey);
  }
  .contacts__icon {
    width: 24px; height: 20px;
    margin-right: 18px;
    fill: var(--detail-grey);
    flex: none;
  }
</style>
</head>
<body>

<section class="card card--front" aria-label="Card front">
  <svg class="card__art" viewBox="0 0 780 446" aria-hidden="true">
    <rect width="780" height="446" fill="var(--paper-white)"/>
    <path d="M545,0 C625,0 622,140 596,205 C566,280 452,300 450,446 L780,446 L780,0 Z" fill="var(--ink-black)"/>
    <clipPath id="front-dark"><path d="M545,0 C625,0 622,140 596,205 C566,280 452,300 450,446 L780,446 L780,0 Z"/></clipPath>
    <g clip-path="url(#front-dark)">
      <circle cx="720" cy="110" r="150" fill="var(--soft-black)"/>
      <circle cx="660" cy="440" r="170" fill="var(--soft-black)"/>
    </g>
  </svg>
  <div class="wordmark">The Velvet Parlour</div>
</section>

<section class="card card--back" aria-label="Card back">
  <svg class="card__art" viewBox="0 0 780 446" aria-hidden="true">
    <rect width="780" height="446" fill="var(--ink-black)"/>
    <circle cx="150" cy="470" r="260" fill="var(--soft-black)"/>
    <path d="M780,110 C700,110 580,120 540,200 C505,275 575,320 560,446 L780,446 Z" fill="var(--paper-white)"/>
  </svg>

  <div class="wordmark">The Velvet Parlour</div>

  <div class="holder">
    <p class="holder__name">Pieter Vandomme</p>
    <p class="holder__title">FOUNDER</p>
  </div>

  <ul class="contacts">
    <li class="contacts__item">
      <svg class="contacts__icon" viewBox="0 0 24 20" aria-hidden="true">
        <path d="M2,6 C2,2 22,2 22,6 L22,8 L17,8 L17,6 L7,6 L7,8 L2,8 Z"/>
        <path d="M6,9 L18,9 L21,18 L3,18 Z"/>
        <circle cx="12" cy="13.5" r="2.4" fill="var(--ink-black)"/>
      </svg>
      +32 (0) 486 514 362
    </li>
    <li class="contacts__item">
      <svg class="contacts__icon" viewBox="0 0 24 20" aria-hidden="true">
        <path d="M1,3 L23,3 L23,17 L1,17 Z"/>
        <path d="M1,3 L12,11 L23,3" fill="none" stroke="var(--ink-black)" stroke-width="1.5"/>
      </svg>
      pieter@velvet-parlour.example
    </li>
    <li class="contacts__item">
      <svg class="contacts__icon" viewBox="0 0 24 20" aria-hidden="true">
        <path d="M1,1 L23,1 L23,14 L1,14 Z M3,3 L3,12 L21,12 L21,3 Z" fill-rule="evenodd"/>
        <path d="M9,14 L15,14 L16,18 L8,18 Z"/>
      </svg>
      www.velvet-parlour.example
    </li>
  </ul>
</section>

</body>
</html>
```